Climb Past Fog - Hear My Drumbeat Rise

The front book cover. The book will include life lessons I've learned through three breast cancer (Teal Lantern) diagnoses and how to create positivity through adversity. Lessons that most people don't think of until they're hit with a life-altering setback. The chapters include Imposter Syndrome (Teal Lantern Keepers don't have time to debate if they're good enough, they just jump in and get it done because life is too short), Stand Your Ground (stick up for your beliefs and advocate for yourself), The Flip Side of It's All About Me (like an emergency rescuer who must equip themselves first, you need to take care of yourself first). The main message in the book is when others say you CAN'T, I say you CAN! Warrior means being strong no matter what life deals you. I've included a word document with more information.
Updates

Please note: Pink is only to be an accent color. I'd like my brand colors to be included. The title of the book is to be the focus with an image to add to the book cover appeal.

Target Market(s)

professionals with a growth mindset and people going through adversity

Industry/Entity Type

HR, Libraries, Hosppitality,

Font styles to use
Sans Serif

Colors
6B429C
8869AF
B7A5CE
E3DAEB
F3F0F8

Requirements
Must have
• Be original. Cover to be appealing to male and female buyers. Incorporate my purple brand color. Be creative and unique.
Nice to have
• Although I have offered a suggestion, I'm open to a creative cover that wows me.
Should not have
• No cartoon image or stock image

```html
<!DOCTYPE html>
<html lang="en">
<head>
<meta charset="utf-8">
<title>Hear My Drumbeat Rise – Book Cover</title>
<link href="https://fonts.googleapis.com/css2?family=Archivo:wght@700;800&display=swap" rel="stylesheet">
<style>
  :root {
    --page-bg: #f3f0f8;
    --cover-purple: #652d7b;
    --title-gold: #ebb13a;
    --title-white: #ffffff;
    --ink-purple: #4a1f5c;
    --accent-green: #8dbf4f;
    --band-gold: #ebb13a;
    --cover-white: #ffffff;
  }
  * { margin: 0; padding: 0; box-sizing: border-box; }
  html, body {
    width: 1066px;
    height: 1200px;
    overflow: hidden;
    background: var(--page-bg);
  }
  .cover {
    position: absolute;
    left: 133px;
    top: 0;
    width: 800px;
    height: 1200px;
    background: var(--cover-white);
    overflow: hidden;
    font-family: "Archivo", "Helvetica Neue", Arial, sans-serif;
  }
  .cover-field {
    position: absolute;
    inset: 0;
  }
  .title {
    position: absolute;
    left: 0;
    top: 63px;
    width: 100%;
    text-align: center;
    font-weight: 800;
    font-size: 140px;
    line-height: 186px;
    letter-spacing: -0.02em;
    text-shadow: 0 6px 10px rgba(30, 0, 40, 0.35);
  }
  .title-lead { display: block; color: var(--title-gold); }
  .title-line { display: block; color: var(--title-white); }
  .title-underline {
    position: absolute;
    left: 98px;
    top: 594px;
    width: 334px;
    height: 11px;
    background: var(--accent-green);
  }
  .hero-photo {
    position: absolute;
    left: 450px;
    top: 620px;
    width: 350px;
    height: 500px;
    background: linear-gradient(120deg, #d9a78c 0%, #e8c2ae 45%, #f6e1dc 75%, #ffffff 100%);
    border-top-left-radius: 110px;
  }
  .subtitle {
    position: absolute;
    left: 96px;
    top: 838px;
    color: var(--ink-purple);
    font-weight: 700;
    font-size: 34px;
    line-height: 48px;
    letter-spacing: -0.01em;
  }
  .base-rule {
    position: absolute;
    left: 0;
    top: 1123px;
    width: 100%;
    height: 8px;
    background: var(--accent-green);
  }
  .author-band {
    position: absolute;
    left: 0;
    top: 1131px;
    width: 100%;
    height: 69px;
    background: var(--band-gold);
    color: var(--ink-purple);
    font-weight: 700;
    font-size: 25px;
    display: flex;
    align-items: center;
    justify-content: center;
    letter-spacing: 0.01em;
  }
</style>
</head>
<body>
  <main class="cover">
    <svg class="cover-field" width="800" height="1200" viewBox="0 0 800 1200" aria-hidden="true">
      <path d="M0,0 H800 V603 C740,700 600,765 430,765 C250,765 90,710 0,626 Z" fill="var(--cover-purple)"/>
    </svg>

    <h1 class="title">
      <span class="title-lead">Hear My</span>
      <span class="title-line">Drumbeat</span>
      <span class="title-line">Rise!</span>
    </h1>
    <div class="title-underline"></div>

    <div class="hero-photo" role="img" aria-label="Photo of a raised arm flexing its bicep, wearing a pale pink t-shirt sleeve"></div>

    <p class="subtitle">Life Lessons<br>from a 3X<br>Teal Lantern<br>Keeper</p>

    <div class="base-rule"></div>
    <div class="author-band">Rae DUNMORE, CRLC, MPAF, CGT</div>
  </main>
</body>
</html>
```